2-Sided Law Firm Business Card

This is the second phase of a law firm "rebrand project" in which I'm changing my firm's name to "Brackwood Law PLLC." The first phase was a logo contest -- I will be updating this project sometime tomorrow with the winning logo design.

The business card will need to include, on its reverse side, the firm's logo and tag line, "Practical Counsel for the Growing Company," on a darker background whose color is consistent with the logo design.

The face of the card will need to include the firm's name (logo), website url, and phone number. It will also need to include, at the very least, the name of the attorney, the attorney's title, the attorney's email address, and the attorney's twitter feed. (I do not maintain a dedicated office and therefore the card does not need to specify a business address.) I will provide the actual contact information to the winning designer. Until then, you may use fictional data in suggesting your proposed design.

My firm specializes in representing startup companies. This means I routinely interact with young entrepreneurs and the (typically) older, more experienced investors who fund them. I need to appeal to the former without offending the latter. I'm interesting in conveying the idea that my firm is a credible alternative to larger, brand-name firms. I use these words in positioning my firm in this market: creative; flexible; fair; practical; experienced. The winning design needs to convey this idea.

I'm will also be re-working my website soon and will likely use noto sans and noto serif as my primary website fonts. I'd like the business card to use a font that is similar, but also compatible with the font used in the firm's logo.

Target Market(s)

Young entrepreneurs and older investors who collaborate in the formation and funding of high-tech startup companies located in the Pacific Northwest.

Industry/Entity Type

Law Firm

Font styles to use
Serif
Sans Serif

Requirements
Must have
• Firm logo, firm tag line, firm website url, firm phone number, attorney name, attorney title, attorney email address, and attorney twitter.

The attached pdf indicates kind of what I have in mind, recognizing that it is my amateur attempt at doing what I'm hoping the winning designer is able to do so much better.
Nice to have
• Adding a statement about my practice areas, if there's room, might be nice:

"General Counsel | Business Formation | Intellectual Property | Angel Investments & Venture Capital | Mergers & Acquisitions"

Also, I make it a point to meet with clients "by appointment only" in the following areas of Seattle: "Alder Bay | Cedar Point | Fernhill | North Quarry." It might be worth including as well, but only if the card itself isn't too cramped. I favor "too simple" over "too informative."
Should not have
• Do NOT put the scales of justice anywhere on this business card. I am a business lawyer.

```html
<!DOCTYPE html>
<html lang="en">
<head>
<meta charset="utf-8">
<title>Brackwood Law PLLC – Business Card</title>
<link rel="stylesheet" href="https://fonts.googleapis.com/css2?family=Open+Sans:ital,wght@0,400;0,600;0,700;1,400&display=swap">
<style>
  :root {
    --page: #d9d9db;
    --paper: #ffffff;
    --charcoal: #2b2b2d;
    --blue: #2f4fb0;
    --ink: #2a2a2a;
    --muted: #d0d0d0;
    --tagline: #9fb0e6;
  }
  * { box-sizing: border-box; margin: 0; padding: 0; }
  html, body { width: 1200px; height: 873px; overflow: hidden; }
  body {
    background: var(--page);
    font-family: "Open Sans", Arial, sans-serif;
    display: flex;
    align-items: center;
    justify-content: center;
    gap: 60px;
  }
  .card {
    position: relative;
    width: 520px;
    height: 297px;
    overflow: hidden;
    box-shadow: 0 6px 18px rgba(0,0,0,.18);
  }

  /* Front */
  .card-front { background: var(--paper); }
  .front-top {
    position: absolute; left: 0; top: 0; width: 100%; height: 96px;
    background: var(--paper);
  }
  .logo-slot {
    position: absolute; left: 28px; top: 22px;
    font-weight: 700; font-size: 15px; color: var(--ink); letter-spacing: .5px;
  }
  .practice-areas {
    position: absolute; left: 120px; right: 24px; top: 18px;
    font-size: 9.5px; line-height: 1.35; color: var(--ink);
  }
  .firm-name {
    position: absolute; right: 26px; top: 64px;
    font-weight: 700; font-size: 15px; color: var(--ink); letter-spacing: .3px;
  }
  .front-band {
    position: absolute; left: 0; top: 96px; width: 100%; height: 150px;
    background: var(--charcoal);
  }
  .contact-list {
    position: absolute; left: 26px; top: 20px;
    list-style: none; color: var(--muted); font-size: 10px;
  }
  .contact-list li { display: flex; align-items: center; gap: 8px; height: 18px; }
  .contact-list svg { width: 12px; height: 12px; flex: none; }
  .contact-list .spacer { width: 12px; flex: none; }
  .attorney {
    position: absolute; right: 26px; bottom: 22px; text-align: right; color: #fff;
  }
  .attorney-name { font-weight: 700; font-size: 20px; letter-spacing: .5px; }
  .attorney-title { font-size: 10px; color: var(--muted); margin-top: 2px; }
  .front-strip {
    position: absolute; left: 0; top: 250px; width: 100%; height: 47px;
    background: var(--blue);
    display: flex; align-items: center; padding-left: 26px;
    color: #e6ebff; font-size: 10.5px;
  }

  /* Back */
  .card-back { background: var(--charcoal); }
  .back-band {
    position: absolute; left: 0; top: 52px; width: 100%; height: 34px;
    background: var(--blue);
    display: flex; align-items: center; padding-left: 24px;
    color: #fff; font-weight: 700; font-size: 17px; letter-spacing: .4px;
  }
  .tagline {
    position: absolute; right: 28px; top: 94px;
    color: var(--tagline); font-size: 10px; font-style: italic;
  }
</style>
</head>
<body>

<section class="card card-front" aria-label="Business card front">
  <div class="front-top">
    <div class="logo-slot">LOGO</div>
    <p class="practice-areas">General Counsel | Business Formation | Intellectual Property<br>Angel Investments &amp; Venture Capital | Mergers &amp; Acquisitions</p>
    <div class="firm-name">BRACKWOOD LAW PLLC</div>
  </div>
  <div class="front-band">
    <ul class="contact-list">
      <li>
        <svg viewBox="0 0 12 12" aria-hidden="true"><path fill="#d0d0d0" d="M2.5 1h2l1 2.5-1.3 1a6 6 0 0 0 3.3 3.3l1-1.3L11 7.5v2a1 1 0 0 1-1 1A9 9 0 0 1 1.5 2a1 1 0 0 1 1-1z"/></svg>
        <span>555 - 014 - 2290</span>
      </li>
      <li>
        <svg viewBox="0 0 12 12" aria-hidden="true"><g fill="none" stroke="#d0d0d0" stroke-width="1"><circle cx="6" cy="6" r="5"/><ellipse cx="6" cy="6" rx="2.2" ry="5"/><line x1="1" y1="6" x2="11" y2="6"/></g></svg>
        <span>www.brackwoodlaw.com</span>
      </li>
      <li><span class="spacer"></span><span>info@brackwoodlaw.com</span></li>
      <li>
        <svg viewBox="0 0 12 12" aria-hidden="true"><circle cx="6" cy="6" r="4.5" fill="#d0d0d0"/></svg>
        <span>@BENHALVORSEN</span>
      </li>
    </ul>
    <div class="attorney">
      <div class="attorney-name">BEN HALVORSEN</div>
      <div class="attorney-title">Startup Attorney</div>
    </div>
  </div>
  <div class="front-strip">Alder Bay | Cedar Point | Fernhill | North Quarry</div>
</section>

<section class="card card-back" aria-label="Business card back">
  <div class="back-band">BRACKWOOD LAW PLLC</div>
  <p class="tagline">Practical Counsel for the Growing Company</p>
</section>

</body>
</html>
```